TriVex Business Card Design - double sided -plumbing local plumbing company

We have a Plumbing company where the design was create through Sketch Hive. We would now like a business card designed as well. We want it to be in the colour version of the logo.

Details below for the card.

Phone Number: 0438 615 247
Email: info@trivexplumbing.example.au
Website: https://trivexplumbing.example.au
We really want a sophisticated design that stand out from the other- informative and timeless.

Target Market(s)

local Canberra market

Industry/Entity Type

Plumbing, gas fitting, hot water

Contact Information for Business Card

Phone number, email, logo and "Supplying all your heating, cooling and hot water needs"

Requirements
Must have
• bust be colourful, must also be though about it being printed on a magnet. must Vex with the logo - I dont want the logo and information chucked onto a white canvas I would prefer it to be smooth and look purposeful

```html
<!DOCTYPE html>
<html lang="en">
<head>
<meta charset="utf-8">
<title>TriVex Plumbing – Business Card</title>
<link rel="stylesheet" href="https://fonts.googleapis.com/css2?family=Montserrat:wght@500;700;800;900&display=swap">
<style>
  :root {
    --stage: #2b2d30;
    --navy: #0c2146;
    --navy-deep: #081a38;
    --sky: #1ea8e6;
    --amber: #f6a623;
    --white: #ffffff;
    --soft: #dbe6f3;
  }
  * { box-sizing: border-box; margin: 0; padding: 0; }
  html, body { width: 1200px; height: 939px; overflow: hidden; }
  body {
    background: var(--stage);
    font-family: "Montserrat", sans-serif;
    position: relative;
  }
  .card {
    position: absolute;
    width: 630px;
    height: 360px;
    border-radius: 4px;
    box-shadow: 0 18px 40px rgba(0,0,0,.45);
    overflow: hidden;
  }
  /* Front side */
  .card--front { left: 80px; top: 70px; background: var(--navy); }
  .card__texture {
    position: absolute; inset: 0;
    background:
      radial-gradient(ellipse at 30% 20%, rgba(60,100,160,.35), transparent 60%),
      radial-gradient(ellipse at 80% 70%, rgba(40,80,140,.3), transparent 55%),
      linear-gradient(160deg, #10295a 0%, #0b1f44 100%);
  }
  .front__brand {
    position: absolute; left: 0; right: 0; top: 110px;
    text-align: center;
    font-weight: 900;
    font-size: 104px;
    letter-spacing: 2px;
    color: var(--sky);
    line-height: 1;
  }
  .front__tagline {
    position: absolute; left: 0; right: 0; bottom: 58px;
    text-align: center;
    font-weight: 800;
    font-size: 15px;
    letter-spacing: .3px;
    color: var(--white);
    text-transform: uppercase;
  }
  /* Back side */
  .card--back { left: 490px; top: 500px; background: var(--navy-deep); }
  .back__brand {
    position: absolute; right: 40px; top: 36px;
    display: flex; align-items: center; gap: 10px;
    font-weight: 900; font-size: 46px; color: var(--sky); line-height: 1;
  }
  .back__brand-dot {
    width: 22px; height: 22px; border-radius: 50%; background: var(--amber);
  }
  .contact { position: absolute; left: 44px; bottom: 36px; color: var(--white); }
  .contact__name {
    font-weight: 800; font-size: 26px; letter-spacing: 1px; text-transform: uppercase;
  }
  .contact__name-first { color: var(--sky); }
  .contact__name-last { color: var(--amber); }
  .contact__role { font-weight: 500; font-size: 13px; letter-spacing: 1.5px; margin: 4px 0 14px; }
  .contact__list { list-style: none; }
  .contact__item {
    display: flex; align-items: center; gap: 10px;
    font-weight: 500; font-size: 14px; letter-spacing: 1px; color: var(--soft);
    margin-top: 6px;
  }
  .contact__icon { width: 15px; height: 15px; flex: none; fill: var(--sky); }
</style>
</head>
<body>
  <section class="card card--front" aria-label="Business card front">
    <div class="card__texture" role="img" aria-label="Water droplets on a deep navy surface"></div>
    <div class="front__brand">TRIVEX</div>
    <p class="front__tagline">Supplying all your heating, cooling and hot water needs</p>
  </section>

  <section class="card card--back" aria-label="Business card back">
    <div class="back__brand"><span class="back__brand-dot"></span>TRIVEX</div>
    <div class="contact">
      <h1 class="contact__name"><span class="contact__name-first">Reid</span> <span class="contact__name-last">Morgan</span></h1>
      <p class="contact__role">CEO</p>
      <ul class="contact__list">
        <li class="contact__item">
          <svg class="contact__icon" viewBox="0 0 24 24" aria-hidden="true"><path d="M6.6 10.8a15.1 15.1 0 0 0 6.6 6.6l2.2-2.2c.3-.3.7-.4 1-.2 1.1.4 2.3.6 3.6.6.6 0 1 .4 1 1V20c0 .6-.4 1-1 1C10.6 21 3 13.4 3 4c0-.6.4-1 1-1h3.5c.6 0 1 .4 1 1 0 1.3.2 2.5.6 3.6.1.3 0 .7-.2 1z"/></svg>
          0438 615 247
        </li>
        <li class="contact__item">
          <svg class="contact__icon" viewBox="0 0 24 24" aria-hidden="true"><path d="M2 5h20v14H2zm2 2v.5l8 5 8-5V7H4z"/></svg>
          info@trivexplumbing.example.au
        </li>
        <li class="contact__item">
          <svg class="contact__icon" viewBox="0 0 24 24" aria-hidden="true"><path d="M12 2a10 10 0 1 0 0 20 10 10 0 0 0 0-20zm6.9 6h-3a15 15 0 0 0-1.3-4 8 8 0 0 1 4.3 4zM12 4c.8 1.1 1.5 2.5 1.9 4h-3.8c.4-1.5 1.1-2.9 1.9-4zM4.3 14a8 8 0 0 1 0-4h3.4a16 16 0 0 0 0 4zm.8 2h3a15 15 0 0 0 1.3 4 8 8 0 0 1-4.3-4zm3-8h-3a8 8 0 0 1 4.3-4 15 15 0 0 0-1.3 4zM12 20c-.8-1.1-1.5-2.5-1.9-4h3.8c-.4 1.5-1.1 2.9-1.9 4zm2.3-6H9.7a14 14 0 0 1 0-4h4.6a14 14 0 0 1 0 4zm.3 6a15 15 0 0 0 1.3-4h3a8 8 0 0 1-4.3 4zm1.7-6a16 16 0 0 0 0-4h3.4a8 8 0 0 1 0 4z"/></svg>
          www.trivexplumbing.example.au
        </li>
      </ul>
    </div>
  </section>
</body>
</html>
```